New modern website for Kerbline Groundworks

Hi we are an existing company that has a current website http://www.kerblinegroundworks.co.nz/ we are looking to get a new vibrant looking website designed to take us further and gain more customers. We are after a simple easy to use website that does not confuse but we want to make an impact and stand out from the rest

Target Market(s)

Homeowners And Commercial Businesses

Industry/Entity Type

It Company

Coding

Coded - Design and coding required

Number of Pages Required

2 page

```html
<!DOCTYPE html>
<html lang="en">
<head>
<meta charset="utf-8">
<title>Kerbline Groundworks</title>
<link rel="stylesheet" href="https://fonts.googleapis.com/css2?family=Jost:wght@400;500;600&family=Oswald:wght@600;700&display=swap">
<style>
:root{
  --yellow:#f6c319;
  --yellow-dark:#e0ab00;
  --ink:#2b2b2b;
  --text:#555;
  --muted:#8a8a8a;
  --asphalt:#2a2a2a;
  --asphalt-dark:#1d1d1d;
  --footer:#262626;
  --footer-bar:#1a1a1a;
  --light:#efeeec;
  --white:#fff;
}
*{box-sizing:border-box;margin:0;padding:0}
html,body{width:1200px;height:4196px;overflow:hidden}
body{font-family:"Jost",Arial,sans-serif;color:var(--text);background:var(--white);position:relative}
section,header,footer{position:absolute;left:0;width:1200px}
.abs{position:absolute}
.brand{font-family:"Jost",Arial,sans-serif;font-weight:600;color:var(--ink);font-size:26px;letter-spacing:.5px;text-transform:uppercase;display:flex;align-items:center;gap:10px}
.brand-square{width:18px;height:18px;background:var(--ink)}
.btn{display:inline-block;background:var(--yellow);color:var(--ink);font-weight:600;text-transform:uppercase;font-size:13px;padding:8px 16px;letter-spacing:.3px}
/* header */
.site-header{top:0;height:84px;background:var(--white);box-shadow:0 2px 6px rgba(0,0,0,.08);z-index:5}
.site-header .brand{left:100px;top:24px}
.main-nav{right:100px;top:0;display:flex;gap:44px;height:84px;align-items:center;font-size:17px;color:var(--ink)}
.main-nav .active{position:relative}
.main-nav .active:after{content:"";position:absolute;left:0;right:0;bottom:-10px;height:3px;background:var(--yellow)}
/* hero */
.hero{top:84px;height:1181px;background:linear-gradient(180deg,#3a3a3a,var(--asphalt) 60%,var(--asphalt-dark))}
.hero-photo{left:0;top:0;width:1200px;height:720px;background:linear-gradient(180deg,#6f9ed8 0%,#a9c6e6 35%,#8d8a7a 55%,#3b3b3b 80%,#2d2d2d 100%)}
.hero-title{left:0;width:1200px;top:370px;text-align:center;font-family:"Oswald",Impact,sans-serif;color:var(--white);font-size:40px;line-height:48px;text-shadow:0 2px 4px rgba(0,0,0,.5)}
.hero-title em{font-style:normal;color:var(--yellow)}
.hero-arrow{top:330px;width:34px;height:34px;border-radius:50%;background:rgba(255,255,255,.25)}
.trust-bar{left:100px;top:566px;width:1000px;height:92px;background:var(--yellow);display:flex;align-items:center;justify-content:space-between;padding:0 28px}
.trust-bar p{font-size:21px;color:var(--ink)}
.trust-bar .outline{border:2px solid var(--ink);padding:10px 26px;font-size:16px;font-weight:600;color:var(--ink);text-transform:uppercase}
.service-card{top:706px;width:306px;height:352px;background:var(--white)}
.service-card .photo{height:196px}
.service-card h3{font-size:15px;font-weight:600;color:var(--ink);text-transform:uppercase;margin:16px 18px 8px}
.service-card p{font-size:14px;line-height:20px;margin:0 18px 12px}
.service-card .btn{margin-left:18px}
.hero-edge{left:0;top:1166px;width:1200px;height:15px;background:var(--yellow)}
/* welcome */
.welcome{top:1265px;height:570px;background:var(--white)}
.section-title{left:0;width:1200px;text-align:center;font-size:34px;color:var(--ink);font-weight:500}
.section-title span{color:var(--yellow)}
.section-title:after{content:"";display:block;width:60px;height:3px;background:var(--yellow);margin:10px auto 0}
.welcome .section-title{display:flex;justify-content:center;align-items:center;gap:14px}
.welcome .section-title:after{display:none}
.welcome-video{left:100px;top:142px;width:482px;height:308px;border:4px solid #ddd;background:linear-gradient(180deg,#9ab6cf,#8f9a8a 40%,#4e4e4e 70%,#3a3a3a)}
.play{left:222px;top:135px;width:38px;height:38px;border-radius:50%;background:rgba(255,255,255,.5)}
.welcome-copy{left:626px;top:140px;width:474px}
.welcome-copy h3{font-size:20px;font-weight:500;color:var(--ink);line-height:28px;margin-bottom:14px}
.welcome-copy p{font-size:15px;line-height:24px;margin-bottom:18px}
.ticks{list-style:none;margin-bottom:18px}
.ticks li{display:flex;align-items:center;gap:12px;font-size:15px;color:var(--ink);margin-bottom:12px}
.tick{width:18px;height:18px;background:var(--ink);display:flex;align-items:center;justify-content:center}
/* expertise */
.expertise{top:1835px;height:335px;background:linear-gradient(90deg,#5a4326,#3a3129 50%,#6a4d22)}
.expertise .shade{inset:0;background:rgba(0,0,0,.45)}
.expertise .section-title{top:42px;color:var(--white)}
.expertise .section-title span{color:var(--yellow)}
.badge{left:100px;top:140px;width:150px;height:150px;border-radius:50%;background:var(--yellow)}
.expertise p{left:332px;top:160px;width:770px;font-size:20px;line-height:33px;color:var(--white)}
/* projects */
.projects{top:2170px;height:815px}
.projects .section-title{top:46px}
.project{width:300px;height:273px}
.project-overlay{inset:0;background:rgba(0,0,0,.55);color:var(--white);text-align:center;padding:80px 30px 0}
.project-overlay h4{font-size:20px;font-weight:500;margin-bottom:10px}
.project-overlay p{font-size:13px;line-height:18px}
.project-overlay .ring{width:44px;height:44px;border:2px solid var(--white);border-radius:50%;margin:18px auto 0}
.projects .view-all{left:484px;top:717px;width:234px;height:44px;text-align:center;line-height:28px;font-size:15px;border:1px solid var(--ink)}
/* testimonials */
.testimonials{top:2985px;height:485px;background:var(--light)}
.testimonials .section-title{top:40px}
.client{top:160px;width:306px;text-align:center}
.avatar{width:84px;height:84px;border-radius:50%;margin:0 auto 12px;border:3px solid var(--white);background:linear-gradient(180deg,#c9d6e0,#8fa3b3)}
.client h4{font-size:15px;font-weight:500;color:var(--ink)}
.client .handle{font-size:13px;color:var(--yellow-dark)}
.quote-card{top:295px;width:306px;height:126px;background:var(--white);padding:16px 18px;font-size:13px;line-height:19px;box-shadow:0 1px 3px rgba(0,0,0,.08)}
.quote-card.featured{border:2px solid var(--yellow)}
.quote-card .date{font-size:11px;color:var(--muted);margin-top:10px}
/* questions */
.questions{top:3470px;height:405px;background:linear-gradient(180deg,#c7c3b2 0%,#d9b75a 35%,#e7b631 70%,#c9962a 100%)}
.questions h2{left:100px;top:56px;font-size:33px;line-height:40px;font-weight:500;color:var(--ink)}
.questions .intro{left:100px;top:150px;width:300px;font-size:13px;line-height:19px;color:#5b4a1c}
.field{width:306px;height:44px;background:var(--white);font-size:14px;color:var(--muted);padding:12px 14px}
.submit{left:458px;top:244px;width:160px;height:40px;background:#111;color:var(--white);font-size:15px;text-align:center;line-height:40px;font-weight:500}
/* footer */
.site-footer{top:3875px;height:321px;background:var(--footer);color:#ccc}
.site-footer h5{font-size:20px;font-weight:500;color:var(--white)}
.site-footer h5 span{color:var(--yellow)}
.site-footer h5:after{content:"";display:block;width:40px;height:2px;background:var(--yellow);margin-top:6px}
.quick-links{list-style:none;font-size:13px;line-height:31px;margin-top:8px}
.quick-links li:before{content:"› ";color:var(--yellow)}
.quick-links li:first-child{color:var(--yellow)}
.contact-list{list-style:none;font-size:13px;margin-top:10px}
.contact-list li{display:flex;gap:10px;margin-bottom:14px;line-height:18px}
.map{width:268px;height:140px;border:4px solid var(--white);background:linear-gradient(135deg,#b9cde0,#e3e6df 50%,#cfd9c4)}
.site-footer .brand{color:var(--white);font-size:22px;left:858px;top:120px}
.site-footer .brand-square{background:var(--white)}
.footer-bar{left:0;top:265px;width:1200px;height:56px;background:var(--footer-bar);font-size:13px;display:flex;align-items:center;justify-content:space-between;padding:0 100px}
.socials{display:flex;gap:8px}
.socials i{display:block;width:22px;height:22px;border-radius:50%}
</style>
</head>
<body>

<header class="site-header">
  <div class="brand abs"><span class="brand-square"></span>Kerbline Groundworks</div>
  <nav class="main-nav abs">
    <span class="active">Home</span><span>About</span><span>Services</span><span>Projects</span><span>Contact Us</span>
  </nav>
</header>

<section class="hero">
  <div class="hero-photo abs" role="img" aria-label="Road crew laying fresh asphalt beside a paving truck under a blue sky"></div>
  <div class="hero-arrow abs" style="left:40px"></div>
  <div class="hero-arrow abs" style="left:1126px"></div>
  <h1 class="hero-title abs">Setting the standards for<br><em>QUALITY</em> Concrete &amp; Asphalters</h1>
  <div class="trust-bar abs">
    <p>The trusted name for all Concrete &amp; Asphalt Paving in Auckland</p>
    <span class="outline">Check out our work</span>
  </div>
  <article class="service-card abs" style="left:100px">
    <div class="photo" role="img" aria-label="Worker raking asphalt" style="background:linear-gradient(180deg,#8aa9c4,#4d5b6a 60%,#2f2f2f)"></div>
    <h3>Asphalt and concreting work</h3>
    <p>When it comes to asphalt services, you can rest assured we will work around your plans.</p>
    <span class="btn">Read more</span>
  </article>
  <article class="service-card abs" style="left:447px">
    <div class="photo" role="img" aria-label="Labour crew working near traffic cones" style="background:linear-gradient(180deg,#9a8f7c,#6e6152 50%,#c46a2a)"></div>
    <h3>All labour</h3>
    <p>Guiding you throughout the process of our asphalt services, you can count on our team.</p>
    <span class="btn">Read more</span>
  </article>
  <article class="service-card abs" style="left:794px">
    <div class="photo" role="img" aria-label="Excavator digging earth on a site" style="background:linear-gradient(180deg,#8fb1d4,#c48a52 50%,#9a5f30)"></div>
    <h3>Additional services</h3>
    <p>As part of our asphalt services, we are proud to offer a range of related services.</p>
    <span class="btn">Read more</span>
  </article>
  <div class="hero-edge abs"></div>
</section>

<section class="welcome">
  <h2 class="section-title abs" style="top:62px"><span>Welcome To</span><span class="brand" style="color:var(--ink)">Kerbline Groundworks</span></h2>
  <div class="welcome-video abs" role="img" aria-label="Video still of a crew finishing a new asphalt driveway">
    <div class="play abs"></div>
  </div>
  <div class="welcome-copy abs">
    <h3>Your one-stop specialist for driveway construction in Auckland</h3>
    <p>Leading the way for asphalt and concrete works throughout the Auckland region, Dean and the local team from Kerbline Groundworks will go the extra mile for your project.</p>
    <ul class="ticks">
      <li><span class="tick"><svg width="12" height="12" viewBox="0 0 12 12"><path d="M2 6l3 3 5-6" stroke="#fff" stroke-width="2" fill="none"/></svg></span>Personalized service</li>
      <li><span class="tick"><svg width="12" height="12" viewBox="0 0 12 12"><path d="M2 6l3 3 5-6" stroke="#fff" stroke-width="2" fill="none"/></svg></span>Our expertise</li>
      <li><span class="tick"><svg width="12" height="12" viewBox="0 0 12 12"><path d="M2 6l3 3 5-6" stroke="#fff" stroke-width="2" fill="none"/></svg></span>Our expertise</li>
    </ul>
    <span class="btn">Read more</span>
  </div>
</section>

<section class="expertise" role="img" aria-label="Workers spreading hot asphalt with shovels">
  <div class="shade abs"></div>
  <h2 class="section-title abs"><span>Our</span> Expertise</h2>
  <div class="badge abs"></div>
  <p class="abs">We have a reputation with clients in and around&nbsp; Auckland for achieving great results on time and within budget every time. We are proud&nbsp; to share our years of experience.</p>
</section>

<section class="projects">
  <h2 class="section-title abs"><span>Latest</span> Projects</h2>
  <div class="project abs" style="left:0;top:132px;background:linear-gradient(180deg,#7a7a72,#3d3d3a)" role="img" aria-label="Concrete laying project">
    <div class="project-overlay abs">
      <h4>Concrete laying</h4>
      <p>Kerbs poured neatly on site, ready for traffic within days.</p>
      <div class="ring"></div>
    </div>
  </div>
  <div class="project abs" style="left:300px;top:132px;background:linear-gradient(180deg,#4f7a3e,#8e8f86)" role="img" aria-label="Garden path with retaining edge"></div>
  <div class="project abs" style="left:600px;top:132px;background:linear-gradient(180deg,#5e7d4a,#8a7768)" role="img" aria-label="Paved driveway through a garden"></div>
  <div class="project abs" style="left:900px;top:132px;background:linear-gradient(180deg,#a9c1dc,#6d6556 60%,#3a3a3a)" role="img" aria-label="Paving machine with crew"></div>
  <div class="project abs" style="left:0;top:405px;background:linear-gradient(180deg,#7a7d6e,#c7b23c 60%,#5a5a50)" role="img" aria-label="Worker cutting concrete"></div>
  <div class="project abs" style="left:300px;top:405px;background:linear-gradient(180deg,#9ab9d9,#6f8a66 45%,#555 70%)" role="img" aria-label="Marked car park beside a harbour"></div>
  <div class="project abs" style="left:600px;top:405px;background:linear-gradient(180deg,#9cc0e0,#8a7a5e 55%,#b08d62)" role="img" aria-label="Kerb line along a new road edge"></div>
  <div class="project abs" style="left:900px;top:405px;background:linear-gradient(180deg,#b2c8de,#9c9a92 50%,#7a6e5e)" role="img" aria-label="Concrete block retaining wall"></div>
  <span class="btn view-all abs">View all projects</span>
</section>

<section class="testimonials">
  <h2 class="section-title abs"><span>Clients</span> Testimonials</h2>
  <div class="client abs" style="left:100px"><div class="avatar" role="img" aria-label="Client portrait"></div><h4>Mr. Tamar Welby</h4><div class="handle">@twelby</div></div>
  <div class="client abs" style="left:447px"><div class="avatar" role="img" aria-label="Client portrait"></div><h4>Miss Hana Pirell</h4><div class="handle">@hpirell</div></div>
  <div class="client abs" style="left:794px"><div class="avatar" role="img" aria-label="Client portrait"></div><h4>Mr. Ravi Ondell</h4><div class="handle">@rondell</div></div>
  <div class="quote-card featured abs" style="left:100px">“ Great crew, tidy work and fair pricing. Our new driveway was finished on time and looks fantastic.<div class="date">4:04PM – MARCH 19, 2015</div></div>
  <div class="quote-card abs" style="left:447px">“ Friendly team who explained every step. The kerbing and paving around our shop came out really well.<div class="date">4:04PM – MARCH 19, 2015</div></div>
  <div class="quote-card abs" style="left:794px">“ Quick quote, careful work and a clean site at the end. We would happily use them again next year.<div class="date">4:04PM – MARCH 19, 2015</div></div>
</section>

<section class="questions" role="img" aria-label="Golden field with an open road towards hills">
  <h2 class="abs">Any Questions you<br>would like to ask?</h2>
  <p class="intro abs">Our friendly team is happy to answer any questions about driveways, kerbing or paving. Send us a message and we will reply quickly.</p>
  <div class="field abs" style="left:458px;top:130px">Name</div>
  <div class="field abs" style="left:794px;top:130px">Email</div>
  <div class="field abs" style="left:458px;top:184px">Phone</div>
  <div class="field abs" style="left:794px;top:184px">Message</div>
  <div class="submit abs">SUBMIT</div>
</section>

<footer class="site-footer">
  <div class="abs" style="left:100px;top:42px">
    <h5><span>Quick</span> Links</h5>
    <ul class="quick-links"><li>Home</li><li>About</li><li>Services</li><li>Projects</li><li>Contact Us</li></ul>
  </div>
  <div class="abs" style="left:264px;top:42px;width:240px">
    <h5>Contact <span>Details</span></h5>
    <ul class="contact-list">
      <li><svg width="12" height="16" viewBox="0 0 12 16"><path d="M6 0a6 6 0 0 1 6 6c0 4-6 10-6 10S0 10 0 6a6 6 0 0 1 6-6z" fill="#f6c319"/><circle cx="6" cy="6" r="2" fill="#262626"/></svg><span>48 Quarry Lane, Penrose,<br>Auckland 1061</span></li>
      <li><svg width="14" height="14" viewBox="0 0 14 14"><path d="M3 1l3 3-2 2a8 8 0 0 0 4 4l2-2 3 3-2 2C6 13 1 8 1 3z" fill="#f6c319"/></svg>021 555 0147</li>
      <li><svg width="14" height="14" viewBox="0 0 14 14"><path d="M3 1l3 3-2 2a8 8 0 0 0 4 4l2-2 3 3-2 2C6 13 1 8 1 3z" fill="#f6c319"/></svg>09 555 0182</li>
      <li><svg width="14" height="12" viewBox="0 0 14 12"><rect width="14" height="12" fill="#f6c319"/><path d="M0 0l7 6 7-6" stroke="#262626" fill="none"/></svg>info@kerblinegroundworks.co.nz</li>
    </ul>
  </div>
  <div class="abs" style="left:532px;top:42px">
    <h5>Location <span>Map</span></h5>
    <div class="map" style="margin-top:12px" role="img" aria-label="Street map of the Auckland office location"></div>
  </div>
  <div class="brand abs"><span class="brand-square"></span>Kerbline Groundworks</div>
  <div class="footer-bar abs">
    <span>Copyright ©2016 Kerbline Groundworks. All Rights Reserved.</span>
    <div class="socials"><i style="background:#3b5998"></i><i style="background:#1da1f2"></i><i style="background:#0077b5"></i><i style="background:#f7931e"></i></div>
  </div>
</footer>

</body>
</html>
```